Flyer/Pop Up Banner Design

This is a design for a new Muslim youth group with a Street theme.
There is a pop up banner and a double sided A5 flyer. Front is design, other side is a standing order form. All info is in the attachment.

Target Market(s)

Youth Boys 12-19

Industry/Entity Type

Group

```html
<!DOCTYPE html>
<html lang="en">
<head>
<meta charset="utf-8">
<title>The Youth – Kerbside Rise banner</title>
<link rel="stylesheet" href="https://fonts.googleapis.com/css2?family=Delius&family=Permanent+Marker&family=Rubik+Dirt&display=swap">
<style>
  :root {
    --paper: #f2f2f2;
    --paper-edge: #d6d6d6;
    --ink: #111111;
    --white: #ffffff;
    --yellow: #f5c300;
    --lemon: #f8f14a;
    --red: #e2242b;
    --navy: #27275e;
    --green: #2f8a3a;
    --footer: #0b0b0b;
    --link-blue: #3b8fd9;
    --gold: #f2d21b;
  }
  * { margin: 0; padding: 0; box-sizing: border-box; }
  html, body { width: 1200px; height: 3000px; overflow: hidden; }
  body {
    position: relative;
    background: radial-gradient(ellipse at 50% 45%, var(--white) 0%, var(--paper) 55%, var(--paper-edge) 100%);
    font-family: "Delius", "Trebuchet MS", sans-serif;
    color: var(--ink);
  }
  .bands { position: absolute; inset: 0; width: 1200px; height: 3000px; }

  .paint {
    position: absolute; border-radius: 50%;
    filter: blur(2px);
  }
  .paint-yellow-top { left: 330px; top: 10px; width: 300px; height: 150px; background: radial-gradient(closest-side, rgba(245,195,0,.75), rgba(245,195,0,0)); }
  .paint-yellow-left { left: -40px; top: 700px; width: 300px; height: 260px; background: radial-gradient(closest-side, rgba(245,195,0,.85), rgba(245,195,0,0)); }
  .paint-red-left { left: -60px; top: 1060px; width: 260px; height: 260px; background: radial-gradient(closest-side, rgba(226,36,43,.8), rgba(226,36,43,0)); }
  .paint-navy-left { left: -70px; top: 1440px; width: 240px; height: 280px; background: radial-gradient(closest-side, rgba(39,39,94,.8), rgba(39,39,94,0)); }
  .paint-green-right { left: 940px; top: 1520px; width: 320px; height: 220px; background: radial-gradient(closest-side, rgba(47,138,58,.8), rgba(47,138,58,0)); }
  .paint-red-right { left: 980px; top: 1290px; width: 260px; height: 140px; background: radial-gradient(closest-side, rgba(226,36,43,.6), rgba(226,36,43,0)); }

  .header-title {
    position: absolute; left: 40px; top: 26px;
    font-family: "Rubik Dirt", "Delius", sans-serif;
    font-size: 96px; line-height: 1; font-weight: 400; color: var(--ink);
    transform: rotate(-1deg);
  }
  .brand-name {
    position: absolute; right: 28px; top: 40px;
    font-family: "Rubik Dirt", "Delius", sans-serif;
    font-size: 58px; line-height: 1; color: var(--red);
    display: flex; align-items: center; gap: 12px;
  }
  .brand-name .dot { width: 24px; height: 24px; border-radius: 50%; background: var(--red); }

  .photo { position: absolute; box-shadow: 0 4px 14px rgba(0,0,0,.35); }
  .photo-group {
    left: 30px; top: 150px; width: 1130px; height: 770px;
    transform: rotate(-0.8deg);
    background: linear-gradient(180deg, #9a8b72 0%, #6b5d4f 30%, #2b2a2e 65%, #1b1b22 100%);
  }
  .photo-outdoor {
    left: 30px; top: 2270px; width: 560px; height: 330px;
    transform: rotate(1.2deg);
    background: linear-gradient(180deg, #4a5a3a 0%, #6f8a4c 55%, #3b4a2c 100%);
  }
  .photo-indoor {
    left: 600px; top: 2260px; width: 570px; height: 340px;
    transform: rotate(-1.2deg);
    background: linear-gradient(180deg, #b9a98e 0%, #8d7d68 50%, #3a3636 100%);
  }

  .slogan {
    position: absolute; z-index: 2;
    font-family: "Permanent Marker", "Rubik Dirt", sans-serif;
    line-height: 1; white-space: nowrap;
  }
  .slogan-start { left: 80px; top: 955px; font-size: 112px; color: var(--ink); transform: rotate(2deg); }
  .slogan-moving { right: 70px; top: 1135px; font-size: 112px; color: var(--white); transform: rotate(4deg); }
  .slogan-active { left: 90px; top: 1355px; font-size: 112px; color: var(--white); transform: rotate(1.5deg); }
  .slogan-deen {
    right: 30px; top: 1560px; text-align: right;
    font-family: "Delius", sans-serif; font-size: 100px; color: var(--white);
    transform: rotate(8deg); line-height: 1.02;
  }
  .slogan-deen .accent { color: var(--ink); font-size: 130px; }

  .donate-box {
    position: absolute; left: 30px; top: 1920px; width: 1090px; height: 390px;
    background: var(--lemon);
    transform: rotate(-1.5deg);
    padding: 40px 240px 0 30px;
    font-size: 58px; line-height: 1.38; color: var(--ink);
    box-shadow: 0 4px 14px rgba(0,0,0,.25);
  }

  .footer {
    position: absolute; left: 0; top: 2620px; width: 1200px; height: 380px;
    background: var(--footer); color: var(--white);
  }
  .social { position: absolute; font-size: 46px; color: var(--link-blue); display: flex; align-items: center; gap: 14px; }
  .social .square { width: 42px; height: 42px; background: var(--link-blue); }
  .social-friendbook { left: 30px; top: 96px; }
  .social-friendbook .amp { color: var(--white); }
  .social-chirper { left: 600px; top: 52px; }
  .url { position: absolute; font-size: 25px; color: var(--white); }
  .url-friendbook { left: 40px; top: 186px; }
  .url-chirper { left: 600px; top: 122px; }
  .footer-brand {
    position: absolute; left: 480px; top: 210px;
    font-family: "Rubik Dirt", "Delius", sans-serif; font-size: 36px; color: var(--red);
  }
  .website { position: absolute; left: 0; width: 100%; top: 300px; text-align: center; font-size: 30px; color: var(--gold); }
</style>
</head>
<body>
  <svg class="bands" viewBox="0 0 1200 3000" aria-hidden="true">
    <polygon points="20,20 1180,14 1180,118 20,150" fill="var(--white)"/>
    <polygon points="0,930 1200,890 1200,1060 0,1100" fill="var(--yellow)"/>
    <polygon points="70,1120 1200,1090 1200,1290 30,1290" fill="var(--red)"/>
    <polygon points="0,1320 1150,1340 1200,1520 0,1500" fill="var(--navy)"/>
    <polygon points="0,1550 1200,1620 1200,1930 60,1800" fill="var(--green)"/>
  </svg>

  <div class="paint paint-yellow-top" role="img" aria-label="Yellow paint splatter"></div>
  <div class="paint paint-yellow-left" role="img" aria-label="Yellow paint splatter"></div>
  <div class="paint paint-red-left" role="img" aria-label="Red paint splatter"></div>
  <div class="paint paint-red-right" role="img" aria-label="Red paint splatter"></div>
  <div class="paint paint-navy-left" role="img" aria-label="Navy paint splatter"></div>
  <div class="paint paint-green-right" role="img" aria-label="Green paint splatter"></div>

  <header>
    <h1 class="header-title">The Youth</h1>
    <div class="brand-name"><span class="dot"></span>Kerbside Rise</div>
  </header>

  <div class="photo photo-group" role="img" aria-label="Group photo of the youth club members posing together outside a building"></div>

  <p class="slogan slogan-start">Start Now</p>
  <p class="slogan slogan-moving">Get Moving</p>
  <p class="slogan slogan-active">Get Active</p>
  <p class="slogan slogan-deen">Get <span class="accent">Deen</span> &amp;<br>Build Tomorrow</p>

  <p class="donate-box">Help the youth of today build a better future! Start by Donating now or set up a standing order.</p>

  <div class="photo photo-outdoor" role="img" aria-label="Youth playing games outdoors on a field around a campfire"></div>
  <div class="photo photo-indoor" role="img" aria-label="Youth doing an indoor table activity in a hall"></div>

  <footer class="footer">
    <div class="social social-friendbook"><span class="square"></span>Like us on Friendbook <span class="amp">&amp;</span></div>
    <span class="url url-friendbook">http://www.friendbook.example/kerbsiderise</span>
    <div class="social social-chirper">follow us on Chirper <span class="square"></span></div>
    <span class="url url-chirper">http://www.chirper.example/KerbsideRise</span>
    <div class="footer-brand">Kerbside Rise</div>
    <p class="website">Our Website : www.kerbside-rise.org</p>
  </footer>
</body>
</html>
```